Website for AV installation with booking system and e-commerce

Company: Velqora
Tag Line: Audio Visual and Security System Installations
We need a website for an AV company based in Sydney Australia. We specialise in Audio Visual, CCTV (security cameras), and Data Cabling.
The purpose of the website is that customers book their installation online with a live booking system.
We are looking for the following:
- Creative and modern design
- easy to use - keep in mind that the user who will book will have little knowledge in technology.
- clean and organised
- colours to work in well with our logo we also like royal to navy blue, but we are open to other suggested what works well with our logo.
We want customers to be able to add products needed for their installation ie when booking to wall mount their TV they can choose to add a TV bracket and cables to the cart and vise-versa buy a bracket or cables and add to cart the installation.
Tabs to be included:
About us
Gallery
Contact Us
Home
Services (there are three services that we offer - Residential, Corporate and Retail)
Products
Book Online/Cart (checkout)
Temporary website checkout: www.velqora.com.au, please note this is very basic and we do not want a copy of this. This is purely to give you an idea of our company.
Good Luck!
Updates
Target Market(s)
home owners/renters, business owners, archiects/designers, builders
Industry/Entity Type
E-Commerce
Look and feel

```html
<!DOCTYPE html>
<html lang="en">
<head>
<meta charset="utf-8">
<title>Velqora – Audio Visual and Security System Installations</title>
<link href="https://fonts.googleapis.com/css2?family=Mulish:wght@400;500;600;700;800;900&family=Marcellus+SC&display=swap" rel="stylesheet">
<style>
  :root {
    --navy: #0b3563;
    --navy-deep: #072a50;
    --royal: #1f55a0;
    --red: #cc0a12;
    --red-deep: #a5060c;
    --text: #2a2d33;
    --muted: #e4ecf5;
    --strip: #8f9499;
    --white: #ffffff;
  }
  * { box-sizing: border-box; margin: 0; padding: 0; }
  html, body { width: 1200px; height: 1000px; overflow: hidden; background: var(--white); }
  body { position: relative; font-family: "Mulish", sans-serif; color: var(--text); }

  .page-shell {
    position: absolute; left: 103px; top: 92px; width: 990px; height: 750px;
    background: linear-gradient(180deg, #fff 0%, #fff 85%, rgba(255,255,255,0) 100%);
    box-shadow: -5px 0 8px -6px rgba(60,95,135,.45), 5px 0 8px -6px rgba(60,95,135,.45);
  }

  .site-header {
    position: absolute; left: 103px; top: 92px; width: 990px; height: 118px;
    background: linear-gradient(105deg, var(--navy-deep) 0%, var(--navy) 35%, #2c5a8e 68%, #a9bfd4 92%, #d7e1ea 100%);
    overflow: hidden;
  }
  .site-header .sweep { position: absolute; left: 0; top: 0; }
  .brand {
    position: absolute; left: 14px; top: 30px; display: flex; align-items: center; gap: 12px;
    font-weight: 900; font-size: 44px; line-height: 50px; color: var(--white); letter-spacing: .5px;
  }
  .brand .dot { width: 24px; height: 24px; border-radius: 50%; background: var(--red); }
  .tagline {
    position: absolute; left: 353px; top: 52px;
    font-family: "Marcellus SC", serif; font-size: 19px; color: var(--muted); letter-spacing: .5px;
  }
  .contact-line {
    position: absolute; left: 14px; top: 101px;
    font-size: 11px; font-weight: 600; color: var(--muted); letter-spacing: .3px;
  }
  .cart {
    position: absolute; right: 20px; top: 92px; display: flex; align-items: center; gap: 7px;
    font-size: 12px; font-weight: 600; color: var(--white); letter-spacing: .2px;
  }

  .main-nav { position: absolute; left: 103px; top: 216px; width: 162px; }
  .main-nav a {
    display: block; height: 30px; line-height: 30px; padding-left: 14px;
    font-size: 16.5px; font-weight: 700; letter-spacing: 1px; color: var(--navy);
    text-decoration: none; text-transform: uppercase;
  }
  .main-nav a.active {
    background: linear-gradient(180deg, var(--red), var(--red-deep)); color: var(--white); width: 110px;
    border-radius: 0 4px 4px 0;
  }
  .main-nav .caret {
    display: inline-block; margin-left: 7px; vertical-align: middle;
    border-left: 4px solid transparent; border-right: 4px solid transparent; border-top: 4px solid var(--red);
  }
  .quote-btn {
    position: absolute; left: 116px; top: 403px; width: 108px; height: 49px;
    background: linear-gradient(180deg, var(--royal), var(--navy)); border-radius: 8px;
    color: var(--white); text-align: center; text-decoration: none;
    box-shadow: 3px 4px 6px rgba(0,0,0,.35);
  }
  .quote-btn .small { display: block; font-size: 14px; font-weight: 800; padding-top: 5px; line-height: 14px; letter-spacing: .5px; }
  .quote-btn .big { display: block; font-size: 28px; font-weight: 900; line-height: 28px; letter-spacing: .5px; }

  .photo-strip {
    position: absolute; left: 265px; top: 210px; width: 827px; height: 217px;
    background: linear-gradient(180deg, #a7abaf, var(--strip));
  }
  .photo-strip .photo { position: absolute; top: 4px; height: 209px; }
  .photo.cameras { left: 7px; width: 264px; background: linear-gradient(160deg, #7aa9dc, #4473b2 55%, #8db6e0); }
  .photo.lounge { left: 282px; width: 264px; background: linear-gradient(160deg, #d9c8ac, #ece0cf 40%, #b8b2ac 78%, #8f8b88); }
  .photo.cables { left: 557px; width: 264px; height: 207px; background: linear-gradient(160deg, #f6f6f6, #e8eaec 60%, #dadee1); }

  .section-title {
    position: absolute; color: var(--red); font-weight: 800; letter-spacing: .3px; white-space: nowrap;
  }
  .section-title .cap { font-size: 23px; }
  .section-title .sc { font-size: 17px; text-transform: uppercase; }
  .services-title { left: 265px; top: 436px; line-height: 28px; }
  .services-list {
    position: absolute; left: 265px; top: 479px; width: 475px; list-style: none;
    font-size: 13.4px; line-height: 16.8px; letter-spacing: .6px; font-weight: 500;
  }
  .services-list li::before, .quals-list li::before { content: "\2022\00a0"; }

  .quals-title { left: 761px; top: 464px; line-height: 28px; }
  .quals-card {
    position: absolute; left: 751px; top: 489px; width: 317px; height: 181px;
    background: var(--white); border-radius: 10px; overflow: hidden;
    box-shadow: 2px 4px 8px rgba(0,0,0,.4);
  }
  .quals-card .installer {
    position: absolute; left: 0; top: 0; width: 135px; height: 181px;
    background: linear-gradient(170deg, #ececec, #bcc6cf 55%, #2b3b69 100%);
  }
  .quals-list {
    position: absolute; left: 151px; top: 13px; width: 160px; list-style: none;
    font-size: 13.4px; line-height: 16.8px; letter-spacing: .6px; font-weight: 500;
  }

  .live-booking {
    position: absolute; left: 914px; top: 832px; width: 166px; height: 28px;
    background: linear-gradient(180deg, var(--red), var(--red-deep)); color: var(--white);
    text-decoration: none; font-size: 17px; font-weight: 700; letter-spacing: .8px;
    text-align: center; line-height: 28px; box-shadow: 0 2px 4px rgba(0,0,0,.2);
  }
</style>
</head>
<body>
  <div class="page-shell"></div>

  <header class="site-header">
    <svg class="sweep" width="990" height="118" viewBox="0 0 990 118" aria-hidden="true">
      <path d="M0 40 Q320 58 990 70 L990 73 Q320 64 0 52 Z" fill="rgba(255,255,255,.13)"/>
      <path d="M0 118 Q420 92 990 108 L990 118 Z" fill="rgba(0,0,0,.12)"/>
    </svg>
    <div class="brand"><span class="dot"></span>Velqora</div>
    <div class="tagline">Audio Visual And Security System Installations</div>
    <div class="contact-line">Harbour 318, Sydney, New South Wales 2000, Australia &nbsp;|&nbsp; 00 61 2 5550 1847 &nbsp;|&nbsp; hello@velqora.com.au</div>
    <div class="cart">
      <svg width="26" height="20" viewBox="0 0 26 20" aria-hidden="true">
        <path d="M1 2 H5 L8 13 H21 L24 5 H6" fill="none" stroke="#fff" stroke-width="2" stroke-linejoin="round"/>
        <circle cx="9" cy="17" r="2" fill="#fff"/><circle cx="20" cy="17" r="2" fill="#fff"/>
      </svg>
      Your Shopping Cart is Empty
    </div>
  </header>

  <nav class="main-nav">
    <a href="#">Home</a>
    <a href="#" class="active">About Us</a>
    <a href="#">Gallery</a>
    <a href="#">Services<span class="caret"></span></a>
    <a href="#">Products<span class="caret"></span></a>
    <a href="#">Contact Us</a>
  </nav>
  <a href="#" class="quote-btn"><span class="small">REQUEST A</span><span class="big">QUOTE</span></a>

  <div class="photo-strip">
    <div class="photo cameras" role="img" aria-label="Security cameras mounted on a pole against a glass tower"></div>
    <div class="photo lounge" role="img" aria-label="Living room with flat screen TV and tower speakers"></div>
    <div class="photo cables" role="img" aria-label="Assorted audio and video cables and connectors"></div>
  </div>

  <h2 class="section-title services-title"><span class="cap">V</span><span class="sc">elqora services include:</span></h2>
  <ul class="services-list">
    <li>Offer advice/guidance in selecting your new AV equipment</li>
    <li>Wall mount flat screen televisions</li>
    <li>Setup up to 7.1 surround sound speakers</li>
    <li>Surround sound equipment programming including receivers, universal remotes, television etc.</li>
    <li>Running cables through walls and ceilings</li>
    <li>Installing wired/wireless network</li>
    <li>Installing security cameras</li>
    <li>Building/upgrading computers &amp; Installing OS for PC.</li>
    <li>Training using the new equipment &amp; technical support.</li>
    <li>Includes additional technical supports up to 2 calls.</li>
    <li>Works have a 1 Year warranty. Labour Only.</li>
    <li>And many more...</li>
  </ul>

  <h2 class="section-title quals-title"><span class="cap">Q</span><span class="sc">ualifications include:</span></h2>
  <div class="quals-card">
    <div class="installer" role="img" aria-label="Technician in a hard hat installing a security camera"></div>
    <ul class="quals-list">
      <li>Open Registration cable course</li>
      <li>OH&amp;S Certificate</li>
      <li>Public Liability In-surance</li>
      <li>Many years of ex-perience in installing a range of AV equip-ment and more.</li>
    </ul>
  </div>

  <a href="#" class="live-booking">LIVE BOOKING</a>
</body>
</html>
```